2 x Digitize Logo | 2 x Business Cards | 2 x Fridge Magnets

We require 6 deliverables:
1. Residential logo redrawn (same just high quality for large print format).
2. Corporate logo redrawn (minor changes to wording and high quality for large print format).
3. New business card design for Furniture Removals (residential)
4. New business card design for Corporate Relocations (business)
5. New Fridge magnet for Furniture removals (residential)
6. New fridge magnet for Corporate Relocations (business)
1. Residential Logo
a. We require the logo to be translated into a high quality digital image with no modifications.
2. Residential Logo
a. We require the logo to be edited (add the word corporate relocations) be translated into a high quality digital image.
3. Using the resilogo please make a new business card for our business.
a. Please see the web site https://www.brightlanehaulage.com.au for colours and inspiration.
b. The residential business card needs the following information:
i. Business Name (using the residential logo).
ii. Free Call: 1800 BL Haul (the Q, P and Move much be the same colour as the logo).
iii. Website: www.BrightLaneHaulage.com.au
iv. Address: 4/7 Ashgrove Court, VIC 3521
v. Email: move@BrightLaneHaulage.com.au
vi. backof Card:
Review our service
www.RateYourStay.com.au
Services: Local, Country, Interstate | Furniture Removals | Piano, Billiard Tables & Antiques
4. Using the corplogo please make a new business card for our business.
b. The corporate business card needs the following information:
i. Business Name (using the corporate logo).
v. Email: corporate@BrightLaneHaulage.com.au
vi. Back of Card:
Review our service
www.RateYourStay.com.au
Services: Corporate relocations | Office equipment moves | Packing Service | Packing Materials
5. Using the resilogo please make a new fridge magent for our business.
b. The residential fidge magnet needs the following information:
iv. Services: Local, Country, Interstate | Furniture Removals | Piano, Billiard Tables & Antiques
6. Using the corplogo please make a new fridge magent for our business.
b. The corporate fidge magnet needs the following information:
iv. Services: Local, Country, Interstate | Corporate relocations
Target Market(s)
Residential Furniture Removals and Corporate Office relocations
Industry/Entity Type
Business
Contact Information for Business Card
Please see full brief for six items required
Requirements
Must have
- Clean simple, easy to read
Nice to have
- fresh, stand out, eye catching
Should not have
- plain, standard, boring, general

```html
<!DOCTYPE html>
<html lang="en">
<head>
<meta charset="utf-8">
<title>Bright Lane Haulage – Corporate Business Card</title>
<link rel="stylesheet" href="https://fonts.googleapis.com/css2?family=Source+Sans+3:wght@400;600&display=swap">
<style>
  :root {
    --brand-green: #00763b;
    --brand-red: #c0252b;
    --ink: #1c1c1c;
    --paper: #ffffff;
    --backdrop: #ecebe8;
    --font-main: "Source Sans 3", "Myriad Pro", Arial, sans-serif;
  }
  * { box-sizing: border-box; margin: 0; padding: 0; }
  html, body {
    width: 1109px; height: 1200px; overflow: hidden;
    background: var(--backdrop);
    font-family: var(--font-main);
  }
  .stage { position: relative; width: 1109px; height: 1200px; }

  .card {
    position: absolute; width: 652px; height: 402px;
    box-shadow: 0 10px 30px rgba(0,0,0,.18);
    overflow: hidden;
  }
  .card--front { left: 60px; top: 130px; background: var(--paper); }
  .card--back  { left: 397px; top: 640px; background: var(--brand-green); }

  .front-panel { position: absolute; inset: 0; }

  .services { position: absolute; left: 35px; top: 233px; color: var(--paper); }
  .services__title { font-size: 21px; font-weight: 400; letter-spacing: .3px; margin-bottom: 18px; }
  .services__list { list-style: none; font-size: 18.5px; line-height: 23.5px; }
  .services__list li::before { content: "\25CF"; font-size: 13px; margin-right: 6px; vertical-align: 2px; }

  .brand { position: absolute; right: 52px; top: 98px; width: 300px; text-align: center; }
  .brand__name { color: var(--brand-red); font-size: 24px; font-weight: 600; letter-spacing: .4px; text-transform: uppercase; }
  .brand__tagline { color: var(--brand-green); font-size: 21px; font-weight: 400; margin-top: 4px; }

  .contact { position: absolute; right: 24px; top: 266px; list-style: none; text-align: right; color: var(--ink); font-size: 18px; }
  .contact li { display: flex; justify-content: flex-end; align-items: center; gap: 6px; height: 23.5px; }
  .contact li.contact__address { margin-top: 8px; }
  .contact .accent { color: var(--brand-red); font-weight: 600; }
  .contact svg { width: 14px; height: 14px; fill: var(--brand-green); flex: none; }

  .review { position: absolute; left: 0; right: 0; top: 172px; text-align: center; }
  .review__label { color: var(--brand-red); font-size: 20px; }
  .review__url { color: var(--paper); font-size: 25px; margin-top: 2px; }
</style>
</head>
<body>
<main class="stage">
  <section class="card card--front" aria-label="Business card front">
    <svg class="front-panel" viewBox="0 0 652 402" preserveAspectRatio="none" aria-hidden="true">
      <polygon points="0,0 266,0 193,62 335,402 0,402" fill="var(--brand-green)"/>
      <polyline points="266,0 193,62 335,402" fill="none" stroke="var(--brand-red)" stroke-width="3"/>
    </svg>

    <div class="services">
      <h2 class="services__title">SERVICES</h2>
      <ul class="services__list">
        <li>Corporate Relocations</li>
        <li>Office Equipment Moves</li>
        <li>Packing Service</li>
        <li>Packing Materials</li>
      </ul>
    </div>

    <div class="brand">
      <p class="brand__name">Bright Lane Haulage</p>
      <p class="brand__tagline">CORPORATE RELOCATIONS</p>
    </div>

    <ul class="contact">
      <li><span>1800 <span class="accent">BL Haul</span> / 1800 52 41 07</span>
        <svg viewBox="0 0 24 24"><path d="M6.6 10.8a15.1 15.1 0 0 0 6.6 6.6l2.2-2.2a1 1 0 0 1 1-.25 11.4 11.4 0 0 0 3.6.57 1 1 0 0 1 1 1V20a1 1 0 0 1-1 1A17 17 0 0 1 3 4a1 1 0 0 1 1-1h3.5a1 1 0 0 1 1 1c0 1.25.2 2.45.57 3.57a1 1 0 0 1-.25 1z"/></svg></li>
      <li><span>corporate@BrightLaneHaulage.com.au</span>
        <svg viewBox="0 0 24 24"><path d="M2 5h20v14H2z M3.5 6.5 12 13l8.5-6.5" fill="var(--brand-green)" stroke="#fff" stroke-width="1.5"/></svg></li>
      <li><span>www.BrightLaneHaulage.com.au</span>
        <svg viewBox="0 0 24 24"><circle cx="12" cy="12" r="10"/><path d="M7 8c2 0 3 1 3 3s2 2 2 4-1 3-1 4M15 5c0 2 1 3 3 3" fill="none" stroke="#fff" stroke-width="1.6"/></svg></li>
      <li class="contact__address"><span>4/7 Ashgrove Court, VIC 3521</span>
        <svg viewBox="0 0 24 24"><path d="M12 2a7 7 0 0 0-7 7c0 5.2 7 13 7 13s7-7.8 7-13a7 7 0 0 0-7-7zm0 9.5A2.5 2.5 0 1 1 12 6.5a2.5 2.5 0 0 1 0 5z"/></svg></li>
    </ul>
  </section>

  <section class="card card--back" aria-label="Business card back">
    <div class="review">
      <p class="review__label">Review Our Service</p>
      <p class="review__url">www.RateYourStay.com.au</p>
    </div>
  </section>
</main>
</body>
</html>
```